Profesional personal website needs design and business card

I need a business card with my professional name as a logo "Marlo Vitality" for my business. I am a Wellness Coach, consultant and trainer. So it should be professional, wellness oriented and modern.

Target Market(s)

Private clients, governments, corporations. Luxury and high market.

Industry/Entity Type

Health And Wellness

Contact Information for Business Card

Marlo Vitality should be the logo

Colors

Designer to choose colors to be used in the design.

Requirements
Must have
• Marlo Vitality
• Name: Tomás Arribal
• Wellness Coach, Consultant & Trainer.
• Website: www.marlovitality.example
• Phone:
• Spain (+34) 612 480 397
• (USA) +1 (555) 318 2046
Nice to have
• The most important is the design of "Marlo Vitality", as this is going to be my personal brand logo. It should be professional, wellness, high end and actual.
Should not have
• no golds, no baroque style..

```html
<!DOCTYPE html>
<html lang="en">
<head>
<meta charset="utf-8">
<title>Marlo Vitality — Business Card</title>
<link href="https://fonts.googleapis.com/css2?family=EB+Garamond:wght@400;500&display=swap" rel="stylesheet">
<style>
  :root {
    --page-bg: #e9ebee;
    --blue-light: #3a8fd8;
    --blue-mid: #2a66c4;
    --blue-deep: #1f45a6;
    --accent-cyan: #3fa9e2;
    --white: #ffffff;
    --ink-blue: #1d3a93;
    --divider: rgba(255,255,255,0.55);
    --flag-es: #d6202a;
    --flag-us: #2c3f8f;
  }
  * { box-sizing: border-box; margin: 0; padding: 0; }
  html, body {
    width: 1200px; height: 800px; overflow: hidden;
    background: var(--page-bg);
    font-family: "EB Garamond", Garamond, Georgia, serif;
  }
  .canvas {
    width: 1200px; height: 800px;
    display: flex; align-items: center; justify-content: center; gap: 40px;
  }
  .card {
    width: 540px; height: 309px;
    position: relative; overflow: hidden;
    box-shadow: 0 10px 28px rgba(20,30,60,0.25);
    color: var(--white);
  }
  .card-blue {
    position: absolute; inset: 0;
    background:
      radial-gradient(ellipse 45% 55% at 0% 30%, rgba(63,169,226,0.45), transparent 70%),
      radial-gradient(ellipse 40% 50% at 100% 70%, rgba(63,169,226,0.3), transparent 70%),
      linear-gradient(180deg, var(--blue-light) 0%, var(--blue-mid) 45%, var(--blue-deep) 100%);
  }
  .card-back .card-blue {
    background:
      radial-gradient(ellipse 35% 45% at 95% 15%, rgba(63,169,226,0.55), transparent 70%),
      radial-gradient(ellipse 30% 40% at 5% 40%, rgba(63,169,226,0.3), transparent 70%),
      linear-gradient(180deg, var(--blue-light) 0%, var(--blue-mid) 45%, var(--blue-deep) 100%);
  }
  .brand-name {
    font-weight: 500;
    text-transform: uppercase;
    letter-spacing: 0.08em;
    color: var(--white);
    white-space: nowrap;
  }
  /* Front */
  .front-content {
    position: absolute; left: 0; right: 0; top: 0; height: 238px;
    text-align: center;
  }
  .front-content .brand-name {
    position: absolute; left: 0; right: 0; top: 22px;
    font-size: 40px;
  }
  .person-name {
    position: absolute; left: 0; right: 0; top: 78px;
    font-size: 34px; font-weight: 400;
  }
  .person-role {
    position: absolute; left: 0; right: 0; top: 120px;
    font-size: 19px; font-weight: 400;
  }
  .phones {
    position: absolute; left: 0; right: 0; top: 152px;
    display: flex; justify-content: center;
  }
  .phone {
    width: 190px; display: flex; flex-direction: column; align-items: center; gap: 6px;
    font-size: 16px;
  }
  .phone-divider { width: 1px; height: 70px; background: var(--divider); }
  .flag { width: 34px; height: 34px; }
  .web-band {
    position: absolute; left: 0; right: 0; bottom: 0; height: 71px;
    background: var(--white);
    display: flex; align-items: flex-start; justify-content: center; padding-top: 6px;
  }
  .web-address {
    color: var(--ink-blue); font-size: 22px; font-weight: 500; letter-spacing: 0.01em;
  }
  /* Back */
  .card-back .brand-name {
    position: absolute; left: 0; right: 0; top: 50%;
    transform: translateY(-50%);
    text-align: center; font-size: 46px;
  }
</style>
</head>
<body>
<main class="canvas">
  <section class="card card-front" aria-label="Business card front">
    <div class="card-blue" role="img" aria-label="Blue gradient background with soft honeycomb texture"></div>
    <div class="front-content">
      <div class="brand-name">Marlo Vitality</div>
      <div class="person-name">Tomás Arribal</div>
      <div class="person-role">Wellness Coach, Consultant &amp; Trainer</div>
      <div class="phones">
        <div class="phone">
          <svg class="flag" viewBox="0 0 34 34" role="img" aria-label="Spain flag">
            <circle cx="17" cy="17" r="16" fill="var(--flag-es)" stroke="#fff" stroke-width="2"/>
          </svg>
          <span>(+34) 612 480 397</span>
        </div>
        <div class="phone-divider"></div>
        <div class="phone">
          <svg class="flag" viewBox="0 0 34 34" role="img" aria-label="United States flag">
            <circle cx="17" cy="17" r="16" fill="var(--flag-us)" stroke="#fff" stroke-width="2"/>
          </svg>
          <span>+1 (555) 318 2046</span>
        </div>
      </div>
    </div>
    <div class="web-band">
      <span class="web-address">www.marlovitality.example</span>
    </div>
  </section>

  <section class="card card-back" aria-label="Business card back">
    <div class="card-blue" role="img" aria-label="Blue gradient background with soft honeycomb texture"></div>
    <div class="brand-name">Marlo Vitality</div>
  </section>
</main>
</body>
</html>
```